Modern looking signage for dental office.

Exterior signage for passing cars
Updates
Need extra days to review
Target Market(s)
Cars passing by
Font styles to use
Sans Serif
Colors
3276b5
Requirements
Must have
- Logo
- OPEN ON SUTURDAY AND SUNDAY
- NIGHT CLINIC AVAILABLE
- PLEASE USE THE FONT TYPE IN FILE 4 UPLOADED BELOW.
- (847) 302-4496
- Modern looking

```html
<!DOCTYPE html>
<html lang="en">
<head>
<meta charset="utf-8">
<title>Nova Dental – Weekend &amp; Night Clinic Sign</title>
<link rel="stylesheet" href="https://fonts.googleapis.com/css2?family=Raleway:wght@400;500&family=Roboto+Condensed:wght@400&family=Oswald:wght@500&family=Montserrat:wght@700;800&display=swap">
<style>
  :root {
    --ink: #4c494a;
    --ink-soft: #5b5859;
    --teal: #0e86a0;
    --teal-deep: #0a6f86;
    --teal-light: #1597b1;
    --white: #ffffff;
    --paper: #f1f2f3;
    --ribbon-text: #3d3b3c;
  }
  html, body {
    margin: 0;
    padding: 0;
    width: 1200px;
    height: 1000px;
    overflow: hidden;
    background: var(--white);
  }
  .sign {
    position: relative;
    width: 1200px;
    height: 1000px;
    overflow: hidden;
    background: linear-gradient(160deg, #ffffff 0%, var(--paper) 45%, #ffffff 100%);
    font-family: "Montserrat", Arial, sans-serif;
  }
  .backdrop {
    position: absolute;
    inset: 0;
  }
  .brand-mark {
    position: absolute;
    left: 38px;
    top: 35px;
    width: 234px;
    height: 234px;
    border: 3px solid var(--ink);
    border-radius: 50%;
    box-sizing: border-box;
  }
  .brand-name {
    position: absolute;
    left: 302px;
    top: 103px;
    margin: 0;
    font-family: "Raleway", Arial, sans-serif;
    font-weight: 400;
    font-size: 126px;
    line-height: 1;
    letter-spacing: 0;
    color: var(--ink);
    white-space: nowrap;
  }
  .tagline {
    position: absolute;
    left: 390px;
    top: 248px;
    margin: 0;
    font-family: "Roboto Condensed", Arial, sans-serif;
    font-weight: 400;
    font-size: 52px;
    line-height: 1;
    color: var(--ink-soft);
    white-space: nowrap;
  }
  .open-on {
    position: absolute;
    left: 0;
    right: 0;
    top: 424px;
    display: flex;
    align-items: center;
    justify-content: center;
    gap: 34px;
    margin: 0;
    font-weight: 700;
    font-size: 78px;
    line-height: 1;
    letter-spacing: 2px;
    color: var(--white);
    white-space: nowrap;
    text-shadow: 0 3px 6px rgba(0,0,0,0.25);
  }
  .open-on::before,
  .open-on::after {
    content: "";
    width: 300px;
    height: 4px;
    background: linear-gradient(90deg, rgba(255,255,255,0.1), var(--white));
  }
  .open-on::after {
    background: linear-gradient(90deg, var(--white), rgba(255,255,255,0.1));
  }
  .days {
    position: absolute;
    left: 0;
    right: 0;
    top: 506px;
    margin: 0;
    text-align: center;
    font-family: "Oswald", Arial, sans-serif;
    font-weight: 500;
    font-size: 118px;
    line-height: 1;
    letter-spacing: 1px;
    color: var(--white);
    white-space: nowrap;
    text-shadow: 0 4px 8px rgba(0,0,0,0.28);
  }
  .night-ribbon {
    position: absolute;
    left: 50px;
    top: 660px;
    width: 1100px;
    height: 145px;
  }
  .night-note {
    position: absolute;
    left: 0;
    right: 0;
    top: 697px;
    margin: 0;
    text-align: center;
    font-weight: 800;
    font-size: 44px;
    line-height: 1;
    color: var(--ribbon-text);
    white-space: nowrap;
  }
  .call {
    position: absolute;
    left: 0;
    right: 0;
    top: 884px;
    margin: 0;
    display: flex;
    align-items: baseline;
    justify-content: center;
    gap: 34px;
    color: var(--teal);
    font-weight: 800;
    line-height: 1;
    white-space: nowrap;
  }
  .call-label { font-size: 64px; letter-spacing: 1px; }
  .call-number { font-size: 94px; }
</style>
</head>
<body>
  <main class="sign">
    <svg class="backdrop" width="1200" height="1000" viewBox="0 0 1200 1000" aria-hidden="true">
      <defs>
        <linearGradient id="band-fill" x1="0" y1="0" x2="1" y2="1">
          <stop offset="0" stop-color="#0a6f86"/>
          <stop offset="0.5" stop-color="#1597b1"/>
          <stop offset="1" stop-color="#0a6f86"/>
        </linearGradient>
        <linearGradient id="rim-fill" x1="0" y1="0" x2="0" y2="1">
          <stop offset="0" stop-color="#e6e8ea"/>
          <stop offset="1" stop-color="#bfc4c8"/>
        </linearGradient>
        <linearGradient id="ribbon-fill" x1="0" y1="0" x2="0" y2="1">
          <stop offset="0" stop-color="#ffffff"/>
          <stop offset="1" stop-color="#d6dadd"/>
        </linearGradient>
      </defs>
      <path class="band-rim" d="M0 408 Q600 270 1200 408 L1200 888 Q600 808 0 888 Z" fill="url(#rim-fill)"/>
      <path class="teal-band" d="M0 432 Q600 300 1200 432 L1200 870 Q600 790 0 870 Z" fill="url(#band-fill)"/>
      <path class="lower-panel" d="M0 890 Q600 812 1200 890 L1200 1000 L0 1000 Z" fill="#f7f8f9"/>
    </svg>

    <header>
      <div class="brand-mark" aria-hidden="true"></div>
      <h1 class="brand-name">NOVA DENTAL</h1>
      <p class="tagline">MODERN GENERAL DENTISTRY</p>
    </header>

    <h2 class="open-on">OPEN ON</h2>
    <h2 class="days">SATURDAY AND SUNDAY</h2>

    <svg class="night-ribbon" viewBox="0 0 1100 145" aria-hidden="true">
      <path d="M0 50 Q550 -40 1100 50 L1055 95 L1100 140 Q550 40 0 140 L45 95 Z" fill="url(#ribbon-fill)"/>
    </svg>
    <p class="night-note">Night Clinic from 5pm-10pm Available</p>

    <p class="call"><span class="call-label">CALL</span><span class="call-number">847-302-4496</span></p>
  </main>
</body>
</html>
```